Motivationsplakat
Sehr schönes Design und sehr angenehme Zusammenarbeit. Ging umgehend auf meine Wünsche ein. Immer wieder gerne! Vielen Dank!
Zielgruppe
Wir, der SC Wendorf aus der Schweiz, sind ein Fussballverein welcher in der 4. höchsten Liga spielt. Der hier zu erstellende Banner (Fusszeile) ist vorwiegend für die Spieler der 1. Mannschaft, als 'Motivationsspritze' auf diversen Plakaten (z.B. auf A1 Plakat wo die Aufstellung draufgeschrieben wird), gedacht.
Aufgabenstellung
Der Banner (als Fussleiste eines Plakates oder als eigenständiger Banner benutzbar) sollte ein Verhältniss von 1 zu 4 haben (also z.B. 50 cm hoch und 200 cm breit). Auf dem Banner muss das Logo des SC Wendorf drauf sein (im Anhang). Dazu muss es folgende Texte enthalten:
- Saison 2017/18
- Die Leidenschaft und den Verein im Herzen!
Der Spruch sollte als zentrale Botschaft verstanden werden und durch die grafische Gestalltung verstärkt/unterstützt werden.
Im Anhang sende ich ihnen noch ein paar Fotos von Spielern, welche sie eventuell verwenden könnten (muss nicht sein). Es dürften jedoch keine Spielergesichter erkennbar sein, also nur z.B. das Dress.

```html
<!DOCTYPE html>
<html lang="de">
<head>
<meta charset="utf-8">
<title>SC Wendorf – Saison 2017/18</title>
<link rel="stylesheet" href="https://fonts.googleapis.com/css2?family=Barlow:wght@500;600;700&display=swap">
<style>
  :root {
    --night: #0c0f18;
    --navy: #1c2740;
    --stadium-light: #6f8fc4;
    --grass: #6b7a2a;
    --grass-dark: #2a2f14;
    --keeper-green: #3f8a45;
    --keeper-orange: #e07a1c;
    --text: #ffffff;
  }
  html, body {
    margin: 0;
    padding: 0;
    width: 1200px;
    height: 300px;
    overflow: hidden;
    background: var(--night);
  }
  .banner {
    position: relative;
    width: 1200px;
    height: 300px;
    overflow: hidden;
    font-family: "Barlow", "Helvetica Neue", Arial, sans-serif;
    color: var(--text);
  }
  .stadium-backdrop {
    position: absolute;
    inset: 0;
    background:
      radial-gradient(ellipse 360px 200px at 170px 30px, rgba(160,190,235,0.55), transparent 70%),
      radial-gradient(ellipse 520px 150px at 430px 300px, rgba(120,135,40,0.75), transparent 75%),
      linear-gradient(180deg, var(--navy) 0%, #141a2a 45%, var(--grass-dark) 80%, #1a1d10 100%);
  }
  .stadium-backdrop::after {
    content: "";
    position: absolute;
    inset: 0;
    background: linear-gradient(90deg, transparent 0%, transparent 45%, rgba(10,12,18,0.75) 75%, rgba(10,12,18,0.9) 100%);
  }
  .keeper-photo {
    position: absolute;
    left: 0;
    top: 30px;
    width: 340px;
    height: 240px;
    background:
      radial-gradient(circle 42px at 265px 125px, rgba(200,165,90,0.85), transparent 100%),
      radial-gradient(ellipse 70px 55px at 30px 50px, rgba(224,122,28,0.85), transparent 100%),
      radial-gradient(ellipse 180px 90px at 90px 190px, rgba(63,138,69,0.85), transparent 100%);
    -webkit-mask-image: linear-gradient(90deg, #000 70%, transparent 100%);
            mask-image: linear-gradient(90deg, #000 70%, transparent 100%);
  }
  .slogan {
    position: absolute;
    left: 340px;
    width: 520px;
    top: 28px;
    margin: 0;
    text-align: center;
    font-weight: 700;
    font-size: 53px;
    line-height: 53px;
    letter-spacing: 1.5px;
    text-transform: uppercase;
  }
  .season {
    position: absolute;
    left: 340px;
    width: 460px;
    top: 198px;
    margin: 0;
    text-align: center;
    font-weight: 500;
    font-size: 39px;
    letter-spacing: 1.5px;
    text-transform: uppercase;
  }
  .club-name {
    position: absolute;
    left: 905px;
    top: 160px;
    display: flex;
    align-items: center;
    gap: 12px;
    font-weight: 700;
    font-size: 40px;
    letter-spacing: 1px;
    text-transform: uppercase;
    white-space: nowrap;
  }
  .club-name .mark {
    width: 22px;
    height: 22px;
    border-radius: 50%;
    background: var(--text);
  }
</style>
</head>
<body>
  <main class="banner">
    <div class="stadium-backdrop" role="img" aria-label="Nächtliches Fussballstadion mit Flutlicht und Rasen"></div>
    <div class="keeper-photo" role="img" aria-label="Torhüter im grünen Trikot hechtet nach einem goldenen Ball, Gesicht abgewandt"></div>
    <h1 class="slogan">Die Leidenschaft<br>und den<br>Verein im Herzen!</h1>
    <p class="season">Saison 2017/18</p>
    <div class="club-name"><span class="mark"></span>SC Wendorf</div>
  </main>
</body>
</html>
```